KVRo Business Cards

We need a business card design. We are a Technology (Audio Visual) design, sales and installation company. Looking for a double sided design, clean

Contact Information for Business Card

Clean, modern look, 2 sided

Font styles to use
Sans Serif

```html
<!DOCTYPE html>
<html lang="en">
<head>
<meta charset="utf-8">
<title>KVRo Business Cards</title>
<link rel="stylesheet" href="https://fonts.googleapis.com/css2?family=Montserrat:wght@400;500;700;800&display=swap">
<style>
  :root {
    --navy: #1c2f3e;
    --orange: #f29423;
    --white: #ffffff;
    --paper: #e9eaec;
    --grey-text: #6b7580;
  }
  * { margin: 0; padding: 0; box-sizing: border-box; }
  html, body { width: 1200px; height: 913px; overflow: hidden; }
  body {
    background: var(--paper);
    font-family: "Montserrat", sans-serif;
    position: relative;
  }
  .card {
    position: absolute;
    width: 560px;
    height: 320px;
    border-radius: 16px;
    box-shadow: 0 6px 18px rgba(0,0,0,0.18);
    overflow: hidden;
  }
  /* Back side */
  .card-back {
    left: 120px;
    top: 86px;
    background: var(--navy);
    display: flex;
    flex-direction: column;
    align-items: center;
    justify-content: center;
  }
  .card-back .wordmark {
    color: var(--white);
    font-weight: 800;
    font-size: 118px;
    letter-spacing: -2px;
    line-height: 1;
  }
  .card-back .site {
    margin-top: 30px;
    color: var(--white);
    font-weight: 400;
    font-size: 13px;
    letter-spacing: 7px;
  }
  /* Front side */
  .card-front {
    left: 520px;
    top: 506px;
    background: var(--white);
  }
  .card-front .wordmark {
    position: absolute;
    right: 34px;
    top: 26px;
    color: var(--navy);
    font-weight: 800;
    font-size: 64px;
    letter-spacing: -1px;
    line-height: 1;
  }
  .person {
    position: absolute;
    left: 34px;
    top: 176px;
  }
  .person-name {
    font-size: 19px;
    font-weight: 700;
    color: var(--navy);
    letter-spacing: 0.5px;
    text-transform: uppercase;
  }
  .person-name .surname { color: var(--orange); font-weight: 500; }
  .person-role {
    font-size: 10px;
    color: var(--grey-text);
    letter-spacing: 1.5px;
    text-transform: uppercase;
    margin-top: 2px;
    padding-bottom: 6px;
    border-bottom: 2px solid var(--orange);
    width: 110px;
  }
  .contact-list {
    list-style: none;
    margin-top: 8px;
  }
  .contact-list li {
    display: flex;
    align-items: center;
    gap: 10px;
    font-size: 12.5px;
    color: var(--navy);
    line-height: 20px;
  }
  .contact-list svg { width: 13px; height: 13px; flex: none; }
  .divider {
    position: absolute;
    left: 318px;
    top: 192px;
    width: 1.5px;
    height: 52px;
    background: var(--orange);
  }
  .address {
    position: absolute;
    left: 336px;
    top: 200px;
    font-size: 12.5px;
    color: var(--navy);
    line-height: 19px;
  }
  .base-rule {
    position: absolute;
    left: 0;
    right: 0;
    bottom: 22px;
    height: 3px;
    background: var(--orange);
  }
</style>
</head>
<body>
  <section class="card card-back" aria-label="Business card back">
    <div class="wordmark">KVRo</div>
    <div class="site">www.kvro.tech</div>
  </section>

  <section class="card card-front" aria-label="Business card front">
    <div class="wordmark">KVRo</div>

    <div class="person">
      <div class="person-name">Daniel <span class="surname">Whitcombe</span></div>
      <div class="person-role">Director</div>
      <ul class="contact-list">
        <li>
          <svg viewBox="0 0 16 16" aria-hidden="true"><path fill="var(--orange)" d="M3.6 1.5l2.2 2.6-1.3 1.6c.9 2 2.4 3.5 4.4 4.4l1.6-1.3 2.6 2.2-1 2.3C6.600 13.300 2.700 9.400 1.300 3.900z"/></svg>
          (555) 214-0386
        </li>
        <li>
          <svg viewBox="0 0 16 16" aria-hidden="true"><rect x="1" y="3" width="14" height="10" rx="1" fill="var(--orange)"/><path d="M1.5 3.5L8 9l6.5-5.5" fill="none" stroke="var(--white)" stroke-width="1.3"/></svg>
          hello@kvro.tech
        </li>
        <li>
          <svg viewBox="0 0 16 16" aria-hidden="true"><circle cx="8" cy="8" r="7" fill="var(--orange)"/><path d="M1 8h14M8 1c-3 3.5-3 10.5 0 14M8 1c3 3.5 3 10.5 0 14" fill="none" stroke="var(--white)" stroke-width="1"/></svg>
          www.kvro.tech
        </li>
      </ul>
    </div>

    <div class="divider"></div>
    <address class="address" style="font-style:normal">
      1180 Larkspur Way, Suite 200<br>
      Halden, Ohio 45210
    </address>

    <div class="base-rule"></div>
  </section>
</body>
</html>
```